Zielgruppe
Tobias Fink Personal Training.
Personaltraining für Bürotätige / leitende Positionen.
Rücken- und Haltungstraining.
Zielgruppe: Herren mittleren Alters, gehobene Klasse.
Aufgabenstellung
Schlicht, elegant, hochwertig
Gerne Logo eingearbeitet.
Schwarz / Gold / Weiß

```html
<!DOCTYPE html>
<html lang="de">
<head>
<meta charset="utf-8">
<title>Tobias Fink Personal Training – Visitenkarte</title>
<link href="https://fonts.googleapis.com/css2?family=Questrial&display=swap" rel="stylesheet">
<style>
  :root {
    --bg: #3a3e43;
    --card-white: #ffffff;
    --card-dark: #263238;
    --gold: #c9a227;
    --ink: #4a4d52;
    --ink-light: #8a8d91;
    --on-dark: #e6e8ea;
  }
  * { box-sizing: border-box; margin: 0; padding: 0; }
  html, body { width: 1200px; height: 900px; overflow: hidden; }
  body {
    background: var(--bg);
    font-family: "Questrial", "Century Gothic", sans-serif;
    display: flex;
    align-items: center;
    justify-content: center;
    gap: 40px;
  }
  .card {
    width: 540px;
    height: 309px;
    position: relative;
    box-shadow: 0 10px 30px rgba(0,0,0,.35);
  }
  .card--front { background: var(--card-white); }
  .card--back { background: var(--card-dark); }

  .brand-name {
    position: absolute;
    color: var(--gold);
    font-size: 20px;
    line-height: 1.2;
    font-weight: 400;
  }
  .card--front .brand-name {
    left: 40px;
    top: 56px;
    width: 180px;
  }
  .card--back .brand-name {
    left: 0;
    right: 0;
    top: 118px;
    text-align: center;
    font-size: 30px;
  }

  .divider {
    position: absolute;
    left: 250px;
    top: 70px;
    width: 2px;
    height: 200px;
    background: var(--gold);
  }

  .contact {
    position: absolute;
    left: 280px;
    top: 72px;
    color: var(--ink);
    font-size: 12.5px;
    line-height: 1.5;
  }
  .contact__name { font-size: 17px; color: var(--ink-light); line-height: 1.2; }
  .contact__role { font-size: 10px; color: var(--ink-light); margin-bottom: 12px; }
  .contact__address { margin-bottom: 4px; }
  .contact__line { display: flex; align-items: center; gap: 7px; }
  .contact__line svg { width: 10px; height: 10px; fill: var(--gold); flex: none; }

  .web {
    position: absolute;
    left: 0;
    right: 0;
    top: 222px;
    display: flex;
    justify-content: center;
    align-items: center;
    gap: 7px;
    color: var(--on-dark);
    font-size: 12px;
  }
  .web svg { width: 11px; height: 11px; }
</style>
</head>
<body>
  <section class="card card--front">
    <p class="brand-name">Tobias Fink Personal Training</p>
    <div class="divider"></div>
    <div class="contact">
      <p class="contact__name">Lukas Brenner</p>
      <p class="contact__role">Inhaber</p>
      <p class="contact__address">TFPT Ltd<br>Birkenweg 27<br>A-4815 Lindenfeld</p>
      <p class="contact__line">
        <svg viewBox="0 0 10 10"><path d="M2 0.5 L3.6 2.6 L2.8 3.6 Q4 6 6.4 7.2 L7.4 6.4 L9.5 8 L8.2 9.5 Q3.5 9 0.5 1.8 Z"/></svg>
        04471/928 40-12
      </p>
      <p class="contact__line">
        <svg viewBox="0 0 10 10"><rect x="2.5" y="0.5" width="5" height="3"/><rect x="0.5" y="4" width="9" height="4.5"/><rect x="2.5" y="7" width="5" height="2.5"/></svg>
        04471/928 40-19
      </p>
      <p class="contact__line">
        <svg viewBox="0 0 10 10"><rect x="0.5" y="2" width="9" height="6.5"/><path d="M0.5 2 L5 6 L9.5 2" stroke="#fff" stroke-width="1" fill="none"/></svg>
        kontakt@tfpt-training.de
      </p>
    </div>
  </section>

  <section class="card card--back">
    <p class="brand-name">Tobias Fink Personal Training</p>
    <p class="web">
      <svg viewBox="0 0 12 12" fill="none" stroke="#e6e8ea" stroke-width="1"><circle cx="6" cy="6" r="5"/><ellipse cx="6" cy="6" rx="2.2" ry="5"/><path d="M1 6 H11"/></svg>
      www.tfpt-training.de
    </p>
  </section>
</body>
</html>
```